GraniteLoop. Customer needs to know about us, what services we provide & contact us

We are a waste tire recycling company. Our primary focus is on providing a sustainable and cost effective service focusing on: Waste Tire Management, Hassle Free Scheduling for Tire Collection, Mobile Shredding & Special site cleanup services. GraniteLoop will be producing TDF, Clean Tire Wire & further materials.
Please look at https://quorvalwheel.example
Please look at https://bandimacorp.example

This is the look and feel of what we want

I have attached a word document with our website info.

Target Market(s)

Tire Install Companies. Such as paltonhaul.example. TDF Purchasers such as kevrofuel.example.

Industry/Entity Type

Waste Tire Recycling

Coding

Coded - Design and coding required

Number of Pages Required

3 page

Font styles to use
Other font styles liked:
• Look at our logo

Requirements
Must have
• We need a 3 page setup for About Us, Services & Contact Us. Contact us should be a form them can fill out and submit to us Images that are related to waste tire recycling. Clean, modern, innovative.
Nice to have
• The color and feel of the website should work with our logo that we did with artmarketly
Should not have
• Anything progressive, political or "woke"

```html
<!DOCTYPE html>
<html lang="en">
<head>
<meta charset="utf-8">
<title>GraniteLoop – Waste Tire Recycling</title>
<link href="https://fonts.googleapis.com/css2?family=Bebas+Neue&family=Poppins:ital,wght@0,400;0,500;0,600;0,700;1,400&display=swap" rel="stylesheet">
<style>
:root{
  --green:#1a9a48;
  --green-dark:#13803b;
  --ink:#1b1b1b;
  --text:#3d3d3d;
  --light:#edf1f4;
  --white:#fff;
  --head:"Bebas Neue",sans-serif;
  --body:"Poppins",sans-serif;
}
*{box-sizing:border-box;margin:0;padding:0}
html,body{width:1200px;height:5254px;overflow:hidden}
body{position:relative;font-family:var(--body);color:var(--text);background:var(--white)}
.abs{position:absolute}
.brand{display:flex;align-items:center;gap:8px;font-family:var(--body);font-weight:700;color:var(--green);font-size:26px}
.brand .dot{width:22px;height:22px;border-radius:50%;background:var(--green)}
.btn{display:flex;height:52px;font-family:var(--head);font-size:19px;letter-spacing:.5px;text-decoration:none}
.btn .lbl{background:var(--green);color:#fff;display:flex;align-items:center;padding:0 28px;border-radius:4px 0 0 4px}
.btn .arr{background:var(--ink);width:48px;display:flex;align-items:center;justify-content:center;border-radius:0 4px 4px 0}
.btn.light .arr{background:#fff}
.eyebrow{font-family:var(--head);font-size:34px;color:var(--ink);line-height:1}
.title{font-family:var(--head);font-size:48px;color:var(--ink);line-height:1}
.title em{font-style:normal;color:var(--green)}

.header{top:0;left:0;width:1200px;height:86px;background:#fff}
.nav{left:470px;top:36px;display:flex;gap:28px;font-size:13px;font-weight:600;color:var(--ink)}
.nav .active{color:var(--green)}
.call{right:0;top:0;width:305px;height:86px;background:var(--green);clip-path:polygon(28px 0,100% 0,100% 100%,28px 100%,0 50%);display:flex;align-items:center;padding-left:38px;gap:14px;color:#fff}
.call .ico{width:50px;height:50px;border-radius:50%;border:2px solid #fff;display:flex;align-items:center;justify-content:center}
.call small{display:block;font-size:13px}
.call b{font-family:var(--head);font-size:24px;font-weight:400;letter-spacing:.5px}

.hero{top:86px;left:0;width:1200px;height:614px;background:radial-gradient(ellipse at 70% 40%,#3a3a3a,#1e1e1e 70%)}
.hero h1{left:92px;top:152px;font-family:var(--head);font-weight:400;color:#fff;font-size:58px;line-height:1}
.hero h1 span{display:block;font-size:76px}
.hero h1 em{font-style:normal;color:var(--green)}
.hero p{left:92px;top:306px;width:520px;color:#fff;font-size:16px;line-height:1.9}
.slide{left:92px;top:520px;display:flex;align-items:center;gap:10px;color:#fff;font-family:var(--head);font-size:20px}
.slide em{font-style:normal;color:var(--green)}

.about-img{left:115px;top:810px;width:430px;height:460px;border-radius:0 0 60px 0;background:linear-gradient(160deg,#6a6d70,#2b2d2f 55%,#4a4e56)}
.about-text{left:598px;top:830px;width:500px}
.about-text p{font-size:15px;line-height:2.05;margin-top:26px}

.esg{top:1358px;left:0;width:1200px;height:717px;background:var(--green)}
.esg .head{top:80px;width:1200px;text-align:center;color:#fff;font-family:var(--head)}
.esg .head small{display:block;font-size:32px}
.esg .head b{display:block;font-weight:400;font-size:46px;line-height:1.1}
.pill{border:3px solid #fff;border-radius:60px;color:#fff;font-size:15px;line-height:1.75;display:flex;align-items:center}
.num{font-family:var(--head);font-size:130px;color:#fff;line-height:1}

.card{overflow:hidden;border-radius:4px;display:flex;flex-direction:column;justify-content:flex-end;align-items:center;text-align:center;color:#fff;padding-bottom:26px;font-family:var(--head);font-size:22px;line-height:1.3}
.card p{font-family:var(--body);font-size:14px;line-height:1.95;margin:6px 18px 18px}

.stat{top:2790px;left:0;width:1200px;text-align:center}
.stat b{font-family:var(--head);font-weight:400;font-size:112px;color:var(--ink);line-height:1}
.stat small{display:block;font-size:15px;font-weight:600;letter-spacing:2px;color:var(--ink);margin-top:4px}

.tests{top:3545px;left:0;width:1200px;height:640px;background:var(--light)}
.tcard{background:#fff;border-radius:10px;border-bottom:3px solid var(--green);border-right:3px solid var(--green);padding:30px}
.tcard .q{font-family:var(--head);font-size:70px;color:#2a2a2a;line-height:.8}
.tcard p{font-style:italic;font-size:15px;line-height:2.1;margin-top:18px}
.who{display:flex;align-items:center;gap:18px;margin-top:20px}
.who .av{width:82px;height:82px;border-radius:50%;background:linear-gradient(135deg,#7a6a55,#3e3a36)}
.who .stars{color:var(--ink);font-size:16px;letter-spacing:2px}
.who b{display:block;font-family:var(--head);font-weight:400;color:var(--green);font-size:20px}
.who small{font-size:15px}
.tnav{width:48px;height:48px;border-radius:50%;background:#4a4a4a;display:flex;align-items:center;justify-content:center}

.contact{top:4185px;left:0;width:1200px;height:660px;background:radial-gradient(ellipse at 50% 40%,#2e2a27,#151311 75%)}
.contact .head{top:80px;width:1200px;text-align:center;color:#fff;font-family:var(--head)}
.field{background:#fff;height:50px;font-size:14px;color:#555;display:flex;align-items:center;padding:0 18px;justify-content:space-between}

.fhead{font-family:var(--head);font-size:22px;color:var(--ink)}
.flist{list-style:none;font-size:15px;line-height:40px;margin-top:8px}
.fci{display:flex;gap:14px;align-items:flex-start;font-size:15px;line-height:1.7;margin-top:16px}
.fci .i{width:38px;height:38px;flex:none;border-radius:50%;background:var(--green);display:flex;align-items:center;justify-content:center}
.soc{width:38px;height:38px;border-radius:50%;border:2px solid var(--ink)}
</style>
</head>
<body>

<header class="abs header">
  <div class="abs brand" style="left:105px;top:28px"><span class="dot"></span>GraniteLoop</div>
  <nav class="abs nav"><span class="active">HOME</span><span>ABOUT US</span><span>SERVICES</span><span>CONTACT US</span></nav>
  <div class="abs call">
    <span class="ico"><svg width="22" height="22" viewBox="0 0 24 24" fill="none" stroke="#fff" stroke-width="2"><path d="M5 3h4l2 5-3 2a11 11 0 0 0 6 6l2-3 5 2v4a2 2 0 0 1-2 2A17 17 0 0 1 3 5a2 2 0 0 1 2-2z"/></svg></span>
    <div><small>Call Us:</small><b>555-014-2290</b></div>
  </div>
</header>

<section class="abs hero" role="img" aria-label="Dark photo of stacked scrap tires">
  <h1 class="abs">WE ARE A WASTE TIRE<span><em>RECYCLING</em> COMPANY.</span></h1>
  <p class="abs">GraniteLoop is forging the wat towards a more sustainable future through scrap tire collection</p>
  <a class="abs btn light" style="left:92px;top:390px"><span class="lbl">LEARN MORE</span><span class="arr"><svg width="16" height="12" viewBox="0 0 16 12"><path d="M1 6h13M9 1l5 5-5 5" stroke="#111" stroke-width="2" fill="none"/></svg></span></a>
  <div class="abs slide">
    <svg width="26" height="34" viewBox="0 0 26 34"><path d="M22 2 6 17l16 15" stroke="#fff" stroke-width="3" fill="none"/></svg>
    <span><em>02</em>/04</span>
    <svg width="26" height="34" viewBox="0 0 26 34"><path d="M4 2l16 15L4 32" stroke="#fff" stroke-width="3" fill="none"/></svg>
  </div>
</section>
<svg class="abs" style="left:580px;top:560px" width="620" height="145" viewBox="0 0 620 145"><path d="M0 145c30-14 30-14 70-14h380c80 0 140-50 170-131v145z" fill="var(--green)"/></svg>

<div class="abs about-img" role="img" aria-label="Gloved hand holding shredded tire rubber"></div>
<div class="abs about-text">
  <div class="eyebrow">ABOUT US</div>
  <div class="title"><em>GRANITE</em> LOOP</div>
  <p>Every Year The EPA estimates that over 300 million scrap tires are generated annually. GraniteLoop is your sustainable business partner that is leading the way forward with a more sustainable eco-friendly approach to the scarp tire industry. Properly reclaiming and recycling these tires into reusable raw materials protects the environment and public health.</p>
  <a class="btn" style="margin-top:40px;width:188px"><span class="lbl">LEARN MORE</span><span class="arr"><svg width="16" height="12" viewBox="0 0 16 12"><path d="M1 6h13M9 1l5 5-5 5" stroke="#fff" stroke-width="2" fill="none"/></svg></span></a>
</div>

<section class="abs esg">
  <div class="abs head"><small>WE FOCUSED ON</small><b>ESG INITIATIVES</b></div>
  <div class="abs num" style="left:100px;top:262px">1</div>
  <div class="abs pill" style="left:165px;top:270px;width:250px;height:105px;padding-left:30px">Advancing Sustainable products from the scrap tires collected</div>
  <div class="abs num" style="left:92px;top:474px">2</div>
  <div class="abs pill" style="left:165px;top:482px;width:220px;height:105px;padding-left:30px">Advancing Environmental Initiatives</div>
  <div class="abs num" style="left:760px;top:262px">3</div>
  <div class="abs pill" style="left:825px;top:270px;width:250px;height:105px;padding-left:40px">Engaging with our community</div>
  <div class="abs num" style="left:760px;top:474px">4</div>
  <div class="abs pill" style="left:825px;top:482px;width:220px;height:105px;padding-left:30px">Responsible Corporate Governance</div>
  <div class="abs" style="left:440px;top:267px;width:320px;height:320px;border-radius:50%;background:#fff;display:flex;align-items:center;justify-content:center">
    <div style="width:280px;height:280px;border-radius:50%;background:var(--green);display:flex;align-items:center;justify-content:center">
      <div style="width:250px;height:250px;border-radius:50%;background:#fff;display:flex;align-items:center;justify-content:center">
        <div class="brand" style="font-size:28px">GraniteLoop</div>
      </div>
    </div>
  </div>
</section>

<div class="abs" style="left:92px;top:2160px"><div class="eyebrow">SERVICES</div><div class="title"><em>WHAT</em> WE DO</div></div>
<a class="abs btn" style="left:875px;top:2170px;height:50px"><span class="lbl" style="padding:0 30px">VIEW ALL SERVICES</span><span class="arr"><svg width="16" height="12" viewBox="0 0 16 12"><path d="M1 6h13M9 1l5 5-5 5" stroke="#fff" stroke-width="2" fill="none"/></svg></span></a>
<div class="abs card" style="left:92px;top:2290px;width:383px;height:188px;background:linear-gradient(180deg,#6b6b6b,#1f1f1f)" role="img" aria-label="Pile of used tires">WASTE TIRE<br>MANAGEMENT &amp; RECYCLING</div>
<div class="abs card" style="left:92px;top:2495px;width:383px;height:185px;background:linear-gradient(180deg,#6f7f92,#23262b)" role="img" aria-label="Technician inspecting a tire">TIRE REMEDIATION &amp;<br>SPECIAL TIRE CLEAN-UPS</div>
<div class="abs card" style="left:490px;top:2290px;width:300px;height:390px;background:linear-gradient(180deg,#5a4a3c,#1d1a17 60%)" role="img" aria-label="Hands working on a calculator and paperwork">SCHEDULING &amp; BILLING
  <p>GraniteLoop is here to make your day-to-day easier with a seamless scheduling...</p>
  <a class="btn light" style="height:42px;font-size:16px"><span class="lbl" style="padding:0 28px">VIEW MORE</span><span class="arr" style="width:42px"><svg width="16" height="12" viewBox="0 0 16 12"><path d="M1 6h13M9 1l5 5-5 5" stroke="var(--green)" stroke-width="2" fill="none"/></svg></span></a>
</div>
<div class="abs card" style="left:805px;top:2290px;width:300px;height:390px;background:linear-gradient(180deg,#b9bdc2,#2a2c30 75%)" role="img" aria-label="Office desk telephone">FIRST RATE CUSTOMER<br>SUPPORT &amp; SERVICE</div>

<div class="abs stat"><b>300+ MILLION</b><small>SCRAP TIRES ARE GENERATED ANNUALLY</small></div>
<svg class="abs" style="left:92px;top:2825px" width="1013" height="20"><path d="M0 10h228M228 2v16M1013 10H785M785 2v16" stroke="#222" stroke-width="2"/></svg>

<div class="abs" style="left:92px;top:2995px;width:510px">
  <div class="eyebrow">PRODUCTS</div>
  <div class="title"><em>GRANITE</em> TIRE TDF</div>
  <p style="font-size:15px;line-height:2.05;margin-top:20px">GraniteLoop seeks to be one of the leading TDF suppliers to the region. This is a product with a wide range of demand from pulp and paper mills, electrical utilities, industrial boilers to cement and asphalt plants our expertly handled tire-derived fuel is being used and receiving high marks for its ever-expanding list of benefits. From driving boiler efficiency to stamping out emissions, GraniteLoop wants to be your TDF supplier offering additional services to include tire pick-up to TDF drop-off we have your back!</p>
  <a class="btn" style="margin-top:42px;width:184px"><span class="lbl">CONTACT US</span><span class="arr"><svg width="16" height="12" viewBox="0 0 16 12"><path d="M1 6h13M9 1l5 5-5 5" stroke="#fff" stroke-width="2" fill="none"/></svg></span></a>
</div>
<div class="abs" style="left:652px;top:2995px;width:433px;height:468px;border-radius:60px 0 0 0;background:linear-gradient(135deg,#c7462c,#7a2a1d 55%,#2f2a28)" role="img" aria-label="Old tire hanging by a rope on a ship hull"></div>

<section class="abs tests">
  <div class="abs" style="top:88px;width:1200px;text-align:center"><div class="eyebrow">TESTIMONIAL</div><div class="title"><em>WHAT</em> PEOPLE SAY</div></div>
  <div class="abs tcard" style="left:92px;top:205px;width:496px;height:405px">
    <div class="q">“</div>
    <p>Lorem ipsum dolor sit amet, consectetur adipi elit sed do eiusmod tempor incididunt ut labore etdol magna aliqua. Ut enim ad minim veniam, quis nos exercitation ullamco laboris nisi ut aliquip cupid.</p>
    <div class="who"><div class="av" role="img" aria-label="Customer portrait"></div><div><div class="stars">★★★★★</div><b>MARCUS HOLLEND</b><small>Engineer</small></div></div>
  </div>
  <div class="abs tcard" style="left:612px;top:205px;width:493px;height:405px">
    <div class="q">“</div>
    <p>Lorem ipsum dolor sit amet, consectetur adipi elit sed do eiusmod tempor incididunt ut labore etdol magna aliqua. Ut enim ad minim veniam, quis nos exercitation ullamco laboris nisi ut aliquip cupid.</p>
    <div class="who"><div class="av" role="img" aria-label="Customer portrait"></div><div><div class="stars">★★★★★</div><b>MARCUS HOLLEND</b><small>Engineer</small></div></div>
  </div>
  <div class="abs tnav" style="left:26px;top:355px"><svg width="12" height="18" viewBox="0 0 12 18"><path d="M10 1 2 9l8 8" stroke="#fff" stroke-width="2" fill="none"/></svg></div>
  <div class="abs tnav" style="left:1124px;top:355px"><svg width="12" height="18" viewBox="0 0 12 18"><path d="m2 1 8 8-8 8" stroke="#fff" stroke-width="2" fill="none"/></svg></div>
</section>

<section class="abs contact" role="img" aria-label="Dim tire warehouse background">
  <div class="abs head"><div style="font-size:32px">CONTACT US</div><div style="font-size:46px;line-height:1.1">GET IN TOUCH</div></div>
  <div class="abs field" style="left:258px;top:183px;width:320px">Company Name</div>
  <div class="abs field" style="left:606px;top:183px;width:334px">Email Address</div>
  <div class="abs field" style="left:258px;top:250px;width:320px">Phone No</div>
  <div class="abs field" style="left:606px;top:250px;width:334px">Address for PickUp</div>
  <div class="abs field" style="left:258px;top:315px;width:320px">Number of Tires<svg width="10" height="6"><path d="M0 0h10L5 6z" fill="#333"/></svg></div>
  <div class="abs field" style="left:606px;top:315px;width:334px">Pickup Frequency</div>
  <div class="abs field" style="left:258px;top:383px;width:682px;height:142px;align-items:flex-start;padding-top:16px">Type your message</div>
  <a class="abs btn light" style="left:508px;top:547px;height:50px"><span class="lbl" style="padding:0 32px">SEND NOW</span><span class="arr"><svg width="16" height="12" viewBox="0 0 16 12"><path d="M1 6h13M9 1l5 5-5 5" stroke="#111" stroke-width="2" fill="none"/></svg></span></a>
</section>
<svg class="abs" style="left:0;top:4700px" width="620" height="150" viewBox="0 0 620 150"><path d="M0 0c20 90 80 130 160 130h380c50 0 60 0 80 20H0z" fill="var(--green)"/></svg>

<footer>
  <div class="abs brand" style="left:92px;top:4950px"><span class="dot"></span>GraniteLoop</div>
  <div class="abs" style="left:92px;top:5018px;display:flex;gap:12px" aria-label="Social links">
    <span class="soc"></span><span class="soc"></span><span class="soc"></span>
  </div>
  <div class="abs" style="left:335px;top:4925px"><div class="fhead">QUICK LINKS</div>
    <ul class="flist"><li>• Home</li><li>• About Us</li><li>• Services</li><li>• Contact</li></ul></div>
  <div class="abs" style="left:500px;top:4925px;width:270px"><div class="fhead">CONTACT US</div>
    <div class="fci"><span class="i"><svg width="14" height="18" viewBox="0 0 14 18"><path d="M7 1a6 6 0 0 1 6 6c0 5-6 10-6 10S1 12 1 7a6 6 0 0 1 6-6z" fill="#fff"/><circle cx="7" cy="7" r="2" fill="var(--green)"/></svg></span>Sed ut perspiciatis unde iste natus error sit</div>
    <div class="fci" style="align-items:center"><span class="i"><svg width="16" height="16" viewBox="0 0 24 24"><path d="M5 3h4l2 5-3 2a11 11 0 0 0 6 6l2-3 5 2v4a2 2 0 0 1-2 2A17 17 0 0 1 3 5a2 2 0 0 1 2-2z" fill="#fff"/></svg></span>555-014-2290</div>
    <div class="fci" style="align-items:center"><span class="i"><svg width="16" height="12" viewBox="0 0 16 12"><rect width="16" height="12" rx="2" fill="#fff"/><path d="m1 1 7 6 7-6" stroke="var(--green)" stroke-width="1.5" fill="none"/></svg></span>support@graniteloop.example</div>
  </div>
  <div class="abs" style="left:812px;top:4925px;width:293px"><div class="fhead">NEWSLETTER</div>
    <p style="font-size:14px;line-height:1.8;margin-top:12px">Sign up for our monthly newsletter and receive latest update on your inbox</p>
    <div style="margin-top:18px;display:flex;height:52px;border:1px solid #bbb;border-radius:4px;overflow:hidden">
      <span style="flex:1;display:flex;align-items:center;padding-left:16px;font-size:14px">Email Address</span>
      <span style="width:50px;background:var(--green);display:flex;align-items:center;justify-content:center"><svg width="14" height="16" viewBox="0 0 14 16"><path d="M1 1l12 7-12 7z" fill="#fff"/></svg></span>
    </div>
  </div>
  <div class="abs" style="left:92px;top:5190px;width:1013px;height:1px;background:#ddd"></div>
  <div class="abs" style="top:5206px;width:1200px;text-align:center;font-size:14px">Copyright © 2022 <span style="color:var(--green)">GraniteLoop</span>. All rights reserved.</div>
  <div class="abs" style="left:1127px;top:5184px;width:48px;height:48px;border-radius:50%;background:var(--ink);display:flex;align-items:center;justify-content:center"><svg width="12" height="16" viewBox="0 0 12 16"><path d="M6 15V2M1 7l5-5 5 5" stroke="#fff" stroke-width="2" fill="none"/></svg></div>
</footer>
</body>
</html>
```